Rack Card

Pretty much the same thing as a brochure, just flat, with a front and back. I will attach a picture of one that I made myself but haven't used because I don't like how simple it is. The specifications are as follows:

Full Bleed Size (starting document size)
3.86" x 8.39"
98 x 213 mm
1158 x 2517 pixels

* Finished artwork should use the full bleed dimensions for best results.
Document Trim Size (final size after being cut)
3.74" x 8.27"
95 x 210 mm
1122 x 2481 pixels

* Please be sure to keep all text within the safe margin.
Resolution
300 DPI

These are descriptions from Prellowink.com where I am ordering the printing from.

Industry/Entity Type

Printing

Requirements
Must have
• The light orange background
Website address
phone number 734-561-0483
Nice to have
• Logo front and back

```html
<!DOCTYPE html>
<html lang="en">
<head>
<meta charset="utf-8">
<title>Luz Nueva Coaching – Rack Card</title>
<link href="https://fonts.googleapis.com/css2?family=PT+Sans+Narrow:wght@400;700&family=Dancing+Script:wght@500&display=swap" rel="stylesheet">
<style>
:root{
  --stage:#2a2a2a;
  --paper:#ffffff;
  --cream:#fbeedd;
  --peach:#f0c48a;
  --crimson:#a8192b;
  --crimson-dark:#8f1222;
  --orange:#f39320;
  --orange-deep:#e4701a;
  --gold:#f7a81c;
  --salmon:#e27a55;
  --text:#3a2a1c;
}
*{margin:0;padding:0;box-sizing:border-box}
html,body{width:960px;height:1200px;overflow:hidden;background:var(--stage)}
body{position:relative;font-family:"PT Sans Narrow",sans-serif}
.panel{position:absolute;top:96px;width:465px;height:1008px;background:var(--paper)}
.panel--back{left:13px}
.panel--front{left:482px}
.sheet{position:absolute;left:8px;top:8px;width:449px;height:992px;overflow:hidden}
.cream-field{position:absolute;left:0;right:0;background:radial-gradient(ellipse at 50% 45%,#fdf5ec 0%,var(--cream) 35%,var(--peach) 100%)}
.abs{position:absolute}

/* back side */
.back .cream-field{top:0;height:674px}
.copy{position:absolute;left:34px;width:382px;color:var(--text);font-size:11.6px;line-height:20px;text-align:justify;text-align-last:center}
.copy h2{color:var(--crimson);font-size:15px;line-height:20px;font-weight:700;text-align:center;margin-bottom:3px}
.copy p{margin:0}
.back-footer{position:absolute;left:0;top:674px;width:449px;height:318px;background:var(--crimson)}
.call{position:absolute;left:0;width:449px;text-align:center;color:var(--gold);font-weight:700}
.brand{position:absolute;left:0;width:100%;text-align:center;font-family:"PT Sans Narrow",sans-serif}
.brand-dot{display:inline-block;border-radius:50%;background:var(--orange);border:3px solid #fff;vertical-align:middle}
.brand-name{display:block;color:var(--orange);font-weight:700;letter-spacing:.5px}
.contact{position:absolute;left:0;width:100%;text-align:center}

/* front side */
.top-band{position:absolute;left:0;top:0;width:449px;height:30px;background:var(--orange)}
.top-rule{position:absolute;left:0;top:30px;width:449px;height:6px;background:var(--salmon)}
.hero{position:absolute;left:0;top:36px;width:449px;height:276px;background:var(--crimson)}
.hero-rule{position:absolute;left:0;top:312px;width:449px;height:5px;background:var(--salmon)}
.portrait{position:absolute;left:162px;top:56px;width:124px;height:185px;border:3px solid #fff;background:linear-gradient(160deg,#6b4a3a 0%,#b9876a 45%,#3a2a26 100%)}
.name{position:absolute;left:0;top:253px;width:449px;text-align:center;color:#fff;font-weight:700;font-size:17px;line-height:20px}
.front .cream-field{top:317px;height:640px}
.invite{position:absolute;left:48px;width:353px;text-align:center;color:var(--crimson);font-size:20px;line-height:20px}
.cards{position:absolute;left:96px;top:496px;width:236px;height:192px;border-radius:8px;background:linear-gradient(135deg,var(--orange-deep) 0%,var(--orange) 45%,#f5f0ea 55%,#e9e4de 100%)}
.front-contact{position:absolute;left:0;width:449px;text-align:center;color:var(--crimson);font-size:19px;line-height:28px}
.front-phone{position:absolute;left:0;width:449px;text-align:center;color:var(--crimson);font-weight:700;font-size:36px}
.site-strip{position:absolute;left:0;top:966px;width:449px;height:18px;background:#f6e3c8;text-align:center;font-size:10px;letter-spacing:1px;line-height:18px;color:var(--salmon)}
.bottom-bar{position:absolute;left:0;top:984px;width:449px;height:8px;background:var(--crimson)}
</style>
</head>
<body>

<section class="panel panel--back">
  <div class="sheet back">
    <div class="cream-field"></div>

    <div class="copy" style="top:54px">
      <h2>So, what is a Life-coach??</h2>
      <p>Life-coaching is about bringing the client to a higher energy level in life, helping them realize that they have a choice and that with choice comes power. The power to live a life that’s purposeful, with intention and focus. A Life-coach will help a client take responsibility for their life, motivates the client to move forward towards their goal and holds them accountable for their actions in the process.</p>
      <p>Very likely, you’re considering hiring a life-coach because you are curious and hoping that there is a solution that will lead you to finally discover what it is that you were meant to do, out of all the talents and gifts that you have, which ones to really focus on. It could be that you are unable to handle certain situations or relationships in your life and want some guidance on how to start making changes so that you aren’t feeling stuck or emotionally run down.</p>
    </div>

    <div class="copy" style="top:290px">
      <h2>Now, what’s the difference between a psychologist, a consultant and a life-coach?</h2>
      <p>Let’s look at it like this, psychologists help sick people get well, typically focusing on the past. Life-coaches help people “get great” at living their lives. We don’t dwell on the past; we only see opportunity. The opportunity to improve the present and take the skills learned into the future. Consultants are there to fix, give information. Life-coaches help people figure out what their real goals and priorities are, the secrets to their own happiness, and we push them or support them to move towards those goals.</p>
      <p>In a nutshell, a Life-coach differs because we teach our clients skills that they can take away with them and use whenever they need to, making the future that much brighter.</p>
    </div>

    <div class="copy" style="top:510px">
      <h2>How can coaching help you?</h2>
      <p>Coaching is a solid step forward, with a trained, objective, real human being. A Life-coach doesn’t have anything invested in how you “should” change or whether it is going to affect them. Sometimes your friends can’t help, because they are stuck in the same way. You might feel that they will be judgmental. Sometimes they just don’t have the resources or time or experience to help you. You may even realize that they aren’t really the best people to hear you out or cheer for you from the sidelines.</p>
    </div>

    <div class="back-footer">
      <svg class="abs" style="left:0;top:150px" width="449" height="168" viewBox="0 0 449 168" aria-hidden="true">
        <path d="M0 70 C120 40 230 120 449 20 L449 168 L0 168 Z" fill="var(--crimson-dark)"/>
        <path d="M0 58 C140 30 240 110 449 10 L449 22 C250 122 130 48 0 72 Z" fill="#c12c3a"/>
        <rect x="0" y="150" width="449" height="6" fill="var(--salmon)"/>
        <rect x="0" y="156" width="449" height="12" fill="var(--crimson)"/>
      </svg>
      <div class="call" style="top:40px;font-size:16px">Call Today!</div>
      <div class="call" style="top:56px;font-size:24px;letter-spacing:1px">734-561-0483</div>
      <div class="brand" style="top:104px">
        <span class="brand-dot" style="width:38px;height:38px"></span>
        <span class="brand-name" style="font-size:18px;margin-top:6px">Luz Nueva Coaching Services</span>
      </div>
      <div class="contact" style="top:236px;color:var(--gold);font-size:13.5px;line-height:16px">
        P.O BOX 4290<br>Clearbrook, NJ 08817<br>Marisol@luznuevacoaching.com<br>www.luznuevacoaching.com
      </div>
    </div>
  </div>
</section>

<section class="panel panel--front">
  <div class="sheet front">
    <div class="top-band"></div>
    <div class="top-rule"></div>
    <div class="hero"></div>
    <div class="portrait" role="img" aria-label="Portrait photograph of the certified life coach"></div>
    <div class="name">Marisol Vega Tarrant<br>(Certified Life Coach)</div>
    <div class="hero-rule"></div>

    <div class="cream-field"></div>
    <div class="invite" style="top:338px">This is an invitation to have a conversation and see whether we connect. Let’s discuss coaching, where you might be suck and how working with a life coach can help you create the life experience you’ve always wanted.</div>
    <div class="invite" style="top:458px">First session is complimentary.</div>

    <div class="cards" role="img" aria-label="Pair of orange and white business cards"></div>

    <div class="front-contact" style="top:704px">P.O BOX 4290<br>Clearbrook, NJ 08817<br>Marisol@luznuevacoaching.com</div>
    <div class="front-phone" style="top:792px">734-561-0483</div>

    <svg class="abs" style="left:0;top:840px" width="449" height="126" viewBox="0 0 449 126" aria-hidden="true">
      <path d="M0 90 C120 60 260 120 449 40 L449 126 L0 126 Z" fill="var(--orange)"/>
      <path d="M0 84 C130 40 260 100 449 8 L449 40 C260 120 120 60 0 96 Z" fill="var(--crimson)"/>
      <path d="M60 100 C180 70 300 100 449 52 L449 70 C300 116 180 90 60 100 Z" fill="var(--orange-deep)"/>
    </svg>
    <div class="brand" style="top:874px;left:236px;width:200px">
      <span class="brand-dot" style="width:36px;height:36px"></span>
      <span class="brand-name" style="font-size:15px;margin-top:4px;color:var(--crimson)">Luz Nueva Coaching Services</span>
    </div>

    <div class="site-strip">www.luznuevacoaching.com</div>
    <div class="bottom-bar"></div>
  </div>
</section>

</body>
</html>
```